Cutting Board Oil Label

I would like a label created for our custom made cutting board oil. The bottle will be clear and come in several different sizes. I have included the current label we use. We would like the information to stay the same, but more aesthetically pleasing and professionally presented. I am also including our logo and the current label of our biggest competitor.

```html
<!DOCTYPE html>
<html lang="en">
<head>
<meta charset="utf-8">
<title>Cutting Board Conditioner Label</title>
<link rel="stylesheet" href="https://fonts.googleapis.com/css2?family=Libre+Baskerville:wght@700&family=Montserrat:wght@400;500;600;700&display=swap">
<style>
  :root {
    --page: #ffffff;
    --wood-light: #fbd99c;
    --wood-mid: #f5d598;
    --wood-deep: #efcf8e;
    --teal: #38c0cc;
    --ink: #111111;
    --slate: #555555;
    --sun: #c2b71d;
    --white: #ffffff;
  }
  * { margin: 0; padding: 0; box-sizing: border-box; }
  html, body {
    width: 1200px; height: 935px; overflow: hidden;
    background: var(--page);
  }
  .label {
    position: absolute; left: 90px; top: 84px;
    width: 1009px; height: 771px;
    display: flex;
  }
  .label-front {
    position: relative;
    width: 745px; height: 100%;
    text-align: center;
    color: var(--ink);
    font-family: "Montserrat", sans-serif;
  }
  .wood-backdrop {
    position: absolute; inset: 0;
    background: linear-gradient(100deg, var(--wood-light) 0%, var(--wood-mid) 55%, var(--wood-deep) 100%);
  }
  .front-content { position: relative; }
  .brand {
    position: absolute; left: 0; right: 0; top: 170px;
    display: flex; justify-content: center; align-items: center; gap: 14px;
    font-family: "Montserrat", sans-serif; font-weight: 600;
    font-size: 40px; color: var(--slate);
  }
  .brand-dot {
    width: 30px; height: 30px; border-radius: 50%;
    background: var(--sun);
  }
  .product-title {
    position: absolute; left: 0; right: 0; top: 225px;
    font-family: "Libre Baskerville", serif; font-weight: 700;
    font-size: 84px; line-height: 118px; letter-spacing: 1px;
  }
  .usage {
    position: absolute; left: 0; right: 0; top: 462px;
    font-weight: 700; font-size: 23.5px; line-height: 34px;
  }
  .claim {
    position: absolute; left: 0; right: 0; top: 565px;
    font-weight: 700; font-size: 45px; letter-spacing: 0.5px;
  }
  .ingredients-heading {
    position: absolute; left: 0; right: 0; top: 621px;
    font-weight: 700; font-size: 19px;
  }
  .ingredients {
    position: absolute; left: 0; right: 0; top: 650px;
    font-weight: 700; font-size: 18.5px;
  }
  .origin, .website {
    position: absolute; top: 707px;
    font-weight: 500; font-size: 23px; color: var(--slate);
  }
  .origin { left: 35px; }
  .website { left: 282px; top: 702px; }
  .label-directions {
    position: relative;
    width: 264px; height: 100%;
    background: var(--teal);
    overflow: hidden;
  }
  .directions-text {
    position: absolute; left: 50%; top: 50%;
    width: 710px; height: 214px;
    transform: translate(-50%, -50%) rotate(-90deg);
    color: var(--white);
    font-family: "Montserrat", sans-serif; font-weight: 400;
    font-size: 19.2px; line-height: 27px;
    text-align: justify; text-align-last: left;
  }
</style>
</head>
<body>
  <div class="label">
    <section class="label-front">
      <div class="wood-backdrop" role="img" aria-label="Light golden wood grain texture background"></div>
      <div class="front-content">
        <div class="brand"><span class="brand-dot"></span><span>Laurel Hollow Goods</span></div>
        <h1 class="product-title">Cutting Board<br>Conditioner</h1>
        <p class="usage">For use on cutting boards, butcher blocks,<br>wood utensils, and any other wood products.</p>
        <p class="claim">FOOD SAFE - ALL NATURAL</p>
        <p class="ingredients-heading">Made with:</p>
        <p class="ingredients">Beeswax, Mineral Oil, Orange Oil, Lemon Oil and Vitamin E</p>
        <p class="origin">Made in the USA</p>
        <p class="website">www.LaurelHollowGoods.com</p>
      </div>
    </section>
    <aside class="label-directions">
      <p class="directions-text">Directions: Apply a generous amount of conditioner with a clean, lint free cloth. For the best results, allow board to soak in conditioner overnight. Using a clean, lint free cloth, buff and remove any excess conditioner. For new or unconditioner cutting boards, butcher blocks, or wodden kitchen utensils we recommend repeating the process a second time to ensure your wood is properly sealed. Recondition about once a month (depending on frequency of use) or when the board begins to become dry to the touch.</p>
    </aside>
  </div>
</body>
</html>
```